35/65

I need a business card for my software development company. I have the logo already and will provide that to you. We create web and mobile applications for businesses. I want it to be an edgy design and am thinking (but not required), just the logo on one side and the contact info on the other.

I will upload your finished file to either InkTorrent or Baa for printing.

Target Market(s)

Business owners who will appreciate an edgy and modern culture in the consultant they hire.

Industry/Entity Type

Software

Requirements
Must have
• Contact info...

Marcus Pell
President
Marcus@3565.co
http://3565.co
555.214.6071
@marcuspgw
Nice to have
• The address is optional. It's...

4725 Larkin Court
Harlow Bay, VA 23499

Also optional are icons next to the email, twitter, phone and URL to clarify what they are (ex: a twitter icon next to @marcuspgw)

```html
<!DOCTYPE html>
<html lang="en">
<head>
<meta charset="utf-8">
<title>35/65 Business Card</title>
<link rel="stylesheet" href="https://fonts.googleapis.com/css2?family=Open+Sans:ital,wght@0,400;0,700;1,400&display=swap">
<style>
  :root {
    --slate: #353c46;
    --slate-deep: #232930;
    --orange: #e8601c;
    --grey-line: #8e8e8e;
    --paper: #ffffff;
    --ink: #1c1c1c;
    --backdrop: #d9d9d9;
  }
  * { box-sizing: border-box; margin: 0; padding: 0; }
  html, body { width: 1200px; height: 900px; overflow: hidden; }
  body {
    background: var(--backdrop);
    font-family: "Open Sans", Arial, sans-serif;
    display: flex;
    flex-direction: column;
    align-items: center;
    justify-content: center;
    gap: 44px;
  }
  .card {
    position: relative;
    width: 640px;
    height: 366px;
    overflow: hidden;
    box-shadow: 0 6px 18px rgba(0,0,0,0.25);
  }
  .card--back { background: var(--slate); }
  .card--front { background: var(--paper); }

  .brand {
    position: absolute;
    left: 0; right: 0;
    text-align: center;
    font-weight: 700;
    letter-spacing: -1px;
    line-height: 1;
  }
  .card--back .brand { top: 110px; font-size: 104px; color: var(--slate-deep); }
  .card--front .brand { top: 58px; font-size: 80px; color: var(--slate); }

  .rule { position: absolute; height: 8px; }
  .card--back .rule { background: var(--grey-line); }
  .card--front .rule { background: var(--slate); }
  .card--back .rule--long { top: 300px; left: 0; width: 560px; }
  .card--back .rule--end { top: 283px; left: 618px; width: 22px; }
  .card--front .rule--long { top: 306px; left: 0; width: 560px; }
  .card--front .rule--end { top: 306px; left: 618px; width: 22px; }

  .accent {
    position: absolute;
    width: 14px;
    height: 10px;
    background: var(--orange);
  }
  .card--back .accent { top: 282px; }
  .card--front .accent { top: 305px; }
  .accent--one { left: 572px; }
  .accent--two { left: 596px; }

  .identity {
    position: absolute;
    right: 330px;
    top: 190px;
    text-align: right;
    color: var(--ink);
    font-size: 14px;
    line-height: 21px;
    white-space: nowrap;
  }
  .identity .name {
    color: var(--orange);
    font-weight: 700;
    font-size: 21px;
    line-height: 28px;
    text-transform: uppercase;
  }
  .identity .title { font-style: italic; }

  .contacts {
    position: absolute;
    left: 345px;
    top: 196px;
    list-style: none;
    color: var(--ink);
    font-size: 14px;
    line-height: 21px;
    white-space: nowrap;
  }
  .contacts li { display: flex; align-items: center; gap: 8px; }
  .contacts svg { width: 14px; height: 14px; flex: none; }
</style>
</head>
<body>

<section class="card card--back" aria-label="Card back">
  <div class="brand">35/65</div>
  <div class="rule rule--long"></div>
  <div class="accent accent--one"></div>
  <div class="accent accent--two"></div>
  <div class="rule rule--end"></div>
</section>

<section class="card card--front" aria-label="Card front">
  <div class="brand">35/65</div>

  <div class="identity">
    <p class="name">Marcus Pell</p>
    <p class="title">President</p>
    <p>4725 Larkin Court</p>
    <p>Harlow Bay, VA 23499</p>
  </div>

  <ul class="contacts">
    <li>
      <svg viewBox="0 0 14 14" aria-hidden="true"><rect width="14" height="14" rx="2" fill="#e8601c"/><path d="M4 3.2 L5.6 3 L6.4 5 L5.4 5.8 Q6.2 7.8 8.2 8.6 L9 7.6 L11 8.4 L10.8 10 Q6.5 10.6 3.4 6.6 Q3.2 4.6 4 3.2 Z" fill="#fff"/></svg>
      555.214.6071
    </li>
    <li>
      <svg viewBox="0 0 14 14" aria-hidden="true"><rect width="14" height="14" rx="2" fill="#e8601c"/><rect x="3" y="4" width="8" height="6" fill="none" stroke="#fff" stroke-width="1.2"/><path d="M3 4 L7 7.5 L11 4" fill="none" stroke="#fff" stroke-width="1.2"/></svg>
      Marcus@3565.co
    </li>
    <li>
      <svg viewBox="0 0 14 14" aria-hidden="true"><rect width="14" height="14" rx="2" fill="#e8601c"/><circle cx="7" cy="7" r="4" fill="none" stroke="#fff" stroke-width="1.1"/><path d="M3 7 H11 M7 3 V11" stroke="#fff" stroke-width="1"/><ellipse cx="7" cy="7" rx="1.8" ry="4" fill="none" stroke="#fff" stroke-width="0.9"/></svg>
      http://3565.co
    </li>
    <li>
      <svg viewBox="0 0 14 14" aria-hidden="true"><rect width="14" height="14" rx="2" fill="#e8601c"/></svg>
      @marcuspgw
    </li>
  </ul>

  <div class="rule rule--long"></div>
  <div class="accent accent--one"></div>
  <div class="accent accent--two"></div>
  <div class="rule rule--end"></div>
</section>

</body>
</html>
```